Web Design for Harbor vNet

Need a website for 24/7 online Tv station. Looking for something unique, fresh and different.

When you click on site, I want viewers to automatically see video player. Video player should take up about 70% screen. Still need sections to show thumbnail clicks of our mission - Inspire, Inform and Entertain. Also need section to highlight new shows or events.

This is a family based TV station that will feature Christian content, news, per pay view movies, music videos, sermons from churches. I want site to appeal to 18 -40 year demo graphic. Even though based in California, I also want site appealing enough to all cultures worldwide.

Go to Streamly and search our channel (harborvnet) for some footages and logo.

Also visit www.harborvnet-demo.com to see logo. Need a design that matches logo.

Updates as of 8/28/13:-

http://video.kindhandsaid-demo.org/channel/animals-agriculture/
KHTV – like the look and feel. Left side to have 16:9 screen with player and on the right will be still pictures slide show

http://www.zuvwatch-demo.com/?camp=XoX512&tracking_ID=000000&K_CLICKID=00000000-0000-0000-0000-000000000000#home/
ZUV – I like the 16:9 screen (I don’t want mine too big – about 60% of screen)
I want a black background that will also match Harbor vNet red and white logo (see uploaded file)
Updates

KHTV – like the look and feel.  Left side to have 16:9 screen with player and on the right will be still pictures slide show

 

Reason: Need more time for poll results to come in and narrow down to one or two designs.

Target Market(s)

zPhone, zTab generation

I like the look and feel Kind Hands Aid TV

Industry/Entity Type

Tv

```html
<!DOCTYPE html>
<html lang="en">
<head>
<meta charset="utf-8">
<title>Harbor vNet</title>
<link href="https://fonts.googleapis.com/css2?family=Source+Sans+3:wght@400;600;700&display=swap" rel="stylesheet">
<style>
  :root {
    --bg: #000000;
    --panel: #161616;
    --panel-dark: #0d0d0d;
    --frame: #1f1f1f;
    --text: #ffffff;
    --muted: #b5b5b5;
    --dim: #8a8a8a;
    --line: #3a3a3a;
    --red: #c4121a;
    --red-dark: #7a0a0e;
  }
  * { box-sizing: border-box; margin: 0; padding: 0; }
  html, body { width: 1200px; height: 992px; overflow: hidden; background: var(--bg); }
  body { font-family: "Source Sans 3", sans-serif; color: var(--text); position: relative; }
  .abs { position: absolute; }

  .account-tabs { left: 844px; top: 0; width: 181px; height: 21px; background: linear-gradient(#3a3a3a, #222); display: flex; align-items: center; justify-content: space-evenly; font-size: 12px; color: var(--muted); border-radius: 0 0 2px 2px; }
  .account-tabs .sep { width: 1px; height: 14px; background: #666; }

  .brand { left: 176px; top: 26px; display: flex; align-items: center; gap: 8px; font-size: 40px; font-weight: 700; color: var(--text); letter-spacing: -1px; }
  .brand-mark { width: 22px; height: 22px; background: var(--red); }

  .rule { height: 0; border-top: 1px dashed var(--line); }
  .main-nav { left: 518px; top: 88px; display: flex; align-items: center; font-size: 16px; letter-spacing: 0.3px; color: var(--muted); }
  .main-nav a { color: inherit; text-decoration: none; }
  .main-nav .active { color: var(--text); }
  .main-nav .sep { width: 1px; height: 15px; background: #444; margin: 0 23px; }

  .search { left: 839px; top: 90px; width: 177px; height: 20px; background: #1b1b1b; border: 1px solid #444; border-radius: 2px; font-size: 11px; color: var(--dim); padding: 2px 7px; }
  .search svg { position: absolute; right: 8px; top: 5px; }

  .stage { left: 118px; top: 342px; width: 956px; height: 650px; background: linear-gradient(#1c1c1c, #141414); }
  .stage-inner { left: 157px; top: 342px; width: 881px; height: 323px; background: linear-gradient(#141414, #232323); }

  .player { left: 173px; top: 148px; width: 855px; height: 504px; background: linear-gradient(#2a2a2a, #121212); }
  .video { left: 182px; top: 157px; width: 833px; height: 435px; background: linear-gradient(100deg, #3b5a8a 0%, #6c7fa8 40%, #c9b7a0 60%, #d8c4a6 80%, #8d8fb8 100%); }
  .play-btn { left: 590px; top: 344px; width: 59px; height: 59px; background: rgba(90,90,90,0.55); border-radius: 8px; }
  .controls { left: 182px; top: 592px; width: 833px; height: 60px; }
  .progress { left: 292px; top: 624px; width: 598px; height: 7px; background: #0a0a0a; border-radius: 4px; }
  .progress-fill { left: 0; top: 0; width: 110px; height: 7px; background: linear-gradient(#e01b22, var(--red-dark)); border-radius: 4px; }

  .section-title { left: 160px; top: 687px; font-size: 17px; letter-spacing: 0.3px; }

  .show-card { width: 199px; height: 181px; top: 717px; background: linear-gradient(#202020, #111); }
  .show-thumb { position: absolute; left: 3px; top: 4px; width: 191px; height: 150px; }
  .show-label { position: absolute; left: 0; right: 0; top: 162px; text-align: center; font-size: 13px; font-weight: 700; color: var(--muted); }

  .footer-copy { left: 163px; top: 950px; font-size: 12px; color: var(--muted); }
  .social { left: 890px; top: 948px; display: flex; gap: 10px; font-size: 12px; color: var(--muted); align-items: center; }
  .social span { display: flex; align-items: center; gap: 4px; }
  .social i { width: 10px; height: 10px; background: #5a5a5a; display: inline-block; }
</style>
</head>
<body>
  <nav class="abs account-tabs"><span>Help</span><span class="sep"></span><span>Sign Up</span><span class="sep"></span><span>Login</span></nav>

  <div class="abs brand"><span>Harbor vNet</span><span class="brand-mark"></span></div>

  <div class="abs rule" style="left:407px;top:83px;width:621px"></div>
  <nav class="abs main-nav">
    <a class="active" href="#">INSPIRE</a><span class="sep"></span>
    <a href="#">INFORM</a><span class="sep"></span>
    <a href="#">ENTERTAIN</a>
  </nav>
  <div class="abs search">Search
    <svg width="8" height="8" viewBox="0 0 8 8"><circle cx="3" cy="3" r="2.2" fill="none" stroke="#aaa" stroke-width="1.2"/><line x1="4.6" y1="4.6" x2="7.5" y2="7.5" stroke="#aaa" stroke-width="1.4"/></svg>
  </div>
  <div class="abs rule" style="left:407px;top:119px;width:621px"></div>

  <div class="abs stage"></div>
  <div class="abs stage-inner"></div>

  <div class="abs player"></div>
  <div class="abs video" role="img" aria-label="Talk show studio scene with guests seated in cream armchairs"></div>
  <div class="abs play-btn">
    <svg width="59" height="59" viewBox="0 0 59 59"><polygon points="24,18 24,41 40,29.5" fill="#2a2a2a"/></svg>
  </div>

  <svg class="abs controls" viewBox="0 0 833 60">
    <rect x="15" y="21" width="7" height="25" fill="#fff"/>
    <rect x="27" y="21" width="7" height="25" fill="#fff"/>
    <polygon points="95,21 80,33.5 95,46" fill="#fff"/>
    <polygon points="110,21 95,33.5 110,46" fill="#fff"/>
    <polygon points="720,21 735,33.5 720,46" fill="#fff"/>
    <polygon points="735,21 750,33.5 735,46" fill="#fff"/>
    <g fill="#fff">
      <polygon points="794,19 805,19 794,30"/>
      <polygon points="822,19 811,19 822,30"/>
      <polygon points="794,47 805,47 794,36"/>
      <polygon points="822,47 811,47 822,36"/>
      <rect x="803" y="28" width="10" height="10"/>
    </g>
  </svg>
  <div class="abs progress"><div class="abs progress-fill"></div></div>

  <div class="abs rule" style="left:148px;top:678px;width:904px"></div>
  <h2 class="abs section-title" style="font-weight:400">FEATURED SHOWS</h2>

  <svg class="abs" style="left:133px;top:786px" width="16" height="28" viewBox="0 0 16 28"><polyline points="14,2 3,14 14,26" fill="none" stroke="#bbb" stroke-width="2"/></svg>
  <svg class="abs" style="left:1041px;top:786px" width="16" height="28" viewBox="0 0 16 28"><polyline points="2,2 13,14 2,26" fill="none" stroke="#bbb" stroke-width="2"/></svg>

  <div class="abs show-card" style="left:160px">
    <div class="show-thumb" role="img" aria-label="Couple embracing beside a waterfall" style="background:linear-gradient(90deg,#3a3f45,#7f9297 55%,#b5c3c7)"></div>
    <div class="show-label">Serial-1</div>
  </div>
  <div class="abs show-card" style="left:381px">
    <div class="show-thumb" role="img" aria-label="Family cast posing together outdoors" style="background:linear-gradient(#7aa0c8,#c9a27d 50%,#3d5a4a)"></div>
    <div class="show-label">Serial-2</div>
  </div>
  <div class="abs show-card" style="left:607px">
    <div class="show-thumb" role="img" aria-label="Singer performing to a crowd" style="background:linear-gradient(#4a4d55,#8b8a8e 50%,#2e2b2e)"></div>
    <div class="show-label">Serial-3</div>
  </div>
  <div class="abs show-card" style="left:832px">
    <div class="show-thumb" role="img" aria-label="Drama cast gathered in a bar" style="background:linear-gradient(#2b2f3c,#6d5a4e 55%,#3b3a3a)"></div>
    <div class="show-label">Serial-4</div>
  </div>

  <div class="abs rule" style="left:148px;top:928px;width:904px"></div>
  <p class="abs footer-copy">© 2103 Harborvnet. | All rights reserved</p>
  <div class="abs social">
    <span><i></i>Friendspace</span>
    <span><i></i>Chirper</span>
    <span><i></i>Streamly</span>
  </div>
</body>
</html>
```